Redesign my business cards

I would like pretty much all the same information as my current business cards but redesigned to stand out more and be more unique photo uploaded to show my current business cards don’t mind if you want to remove or replace I for on the back

```html
<!DOCTYPE html>
<html lang="en">
<head>
<meta charset="utf-8">
<title>Kestrel Detailing – Business Card</title>
<link rel="stylesheet" href="https://fonts.googleapis.com/css2?family=Arvo:wght@700&family=Oswald:wght@700&family=Raleway:wght@500;600;700&display=swap">
<style>
  :root {
    --red: #c4001a;
    --red-deep: #8f0613;
    --black: #000000;
    --ink: #141414;
    --white: #ffffff;
    --grey: #9a9a9a;
    --page: #e8eaee;
  }
  * { margin: 0; padding: 0; box-sizing: border-box; }
  html, body { width: 957px; height: 1200px; overflow: hidden; }
  body { background: var(--page); position: relative; font-family: "Raleway", sans-serif; }

  .card { position: absolute; background: var(--black); overflow: hidden; color: var(--white); }
  .card-bg { position: absolute; inset: 0; width: 100%; height: 100%; }

  /* Front */
  .card-front { left: 31px; top: 47px; width: 897px; height: 538px; }
  .phone-tag {
    position: absolute; left: 36px; top: 36px; padding: 6px 14px;
    background: var(--white); color: var(--black);
    font-family: "Arvo", serif; font-weight: 700; font-size: 24px; line-height: 1.2; letter-spacing: 1px;
  }
  .front-art {
    position: absolute; left: 36px; top: 104px; width: 250px; height: 170px; border-radius: 14px;
    background: linear-gradient(160deg, #2a2a2a 0%, var(--ink) 100%);
  }
  .brand-mark {
    position: absolute; left: 36px; top: 300px; width: 260px;
    font-family: "Arvo", serif; font-weight: 700; font-size: 38px; line-height: 1.15; color: var(--white);
  }
  .brand-sub { position: absolute; left: 36px; top: 410px; width: 40px; height: 40px; border-radius: 50%; background: var(--black); }

  .identity { position: absolute; left: 440px; top: 96px; width: 420px; }
  .identity-name { font-family: "Arvo", serif; font-weight: 700; font-size: 40px; line-height: 1.1; }
  .identity-role { margin-top: 8px; font-size: 24px; font-weight: 500; color: var(--white); }
  .identity-rule { margin-top: 18px; width: 70px; height: 5px; background: var(--red); }

  .contact-list { position: absolute; left: 440px; top: 290px; width: 420px; list-style: none; }
  .contact-row { display: flex; align-items: center; gap: 16px; height: 50px; margin-bottom: 28px; }
  .contact-icon { width: 46px; height: 46px; flex: none; }
  .contact-phone { font-size: 30px; font-weight: 600; letter-spacing: 1px; }
  .contact-email { font-family: "Arvo", serif; font-weight: 700; font-size: 16px; }

  /* Back */
  .card-back { left: 29px; top: 610px; width: 903px; height: 541px; }
  .back-brand {
    position: absolute; left: 32px; top: 44px; width: 220px;
    font-family: "Arvo", serif; font-weight: 700; font-size: 28px; line-height: 1.15;
  }
  .back-art {
    position: absolute; left: 32px; top: 170px; width: 200px; height: 120px; border-radius: 12px;
    background: linear-gradient(160deg, #2a2a2a 0%, var(--ink) 100%);
  }
  .service-row { position: absolute; left: 318px; width: 555px; display: flex; gap: 18px; }
  .price {
    flex: none; width: 64px; height: 64px; border-radius: 50%;
    background: var(--black); border: 4px solid var(--red);
    display: flex; align-items: center; justify-content: center;
    font-family: "Oswald", sans-serif; font-weight: 700; font-size: 20px; color: var(--white);
  }
  .service-title { font-family: "Oswald", sans-serif; font-weight: 700; font-size: 20px; line-height: 1; color: var(--red); margin: 4px 0 6px; }
  .service-desc { font-size: 15.5px; font-weight: 500; line-height: 22px; }
  .divider { position: absolute; left: 318px; width: 555px; height: 1px; background: #3a3a3a; }
</style>
</head>
<body>

<section class="card card-front">
  <svg class="card-bg" viewBox="0 0 897 538" preserveAspectRatio="none" aria-hidden="true">
    <polygon points="0,0 370,0 300,538 0,538" fill="var(--red)"/>
    <polygon points="384,0 396,0 326,538 314,538" fill="var(--red)"/>
  </svg>

  <p class="phone-tag">0412555019</p>
  <div class="front-art" role="img" aria-label="Illustration of a sports car"></div>
  <p class="brand-mark">KESTREL<br>DETAILING</p>

  <div class="identity">
    <h1 class="identity-name">DANIEL HARLOW</h1>
    <p class="identity-role">Owner/Operator</p>
    <div class="identity-rule"></div>
  </div>

  <ul class="contact-list">
    <li class="contact-row">
      <svg class="contact-icon" viewBox="0 0 50 50" aria-hidden="true">
        <circle cx="25" cy="25" r="25" fill="var(--red)"/>
        <path d="M17 15 l5 -1 3 6 -3 2 q2 5 6 7 l2 -3 6 3 -1 5 q-12 1 -18 -19z" fill="var(--white)"/>
      </svg>
      <span class="contact-phone">0412555019</span>
    </li>
    <li class="contact-row">
      <svg class="contact-icon" viewBox="0 0 50 50" aria-hidden="true">
        <circle cx="25" cy="25" r="25" fill="var(--red)"/>
        <rect x="14" y="17" width="22" height="16" rx="3" fill="var(--white)"/>
        <path d="M15 19 l10 7 10 -7" fill="none" stroke="var(--red)" stroke-width="2"/>
      </svg>
      <span class="contact-email">KESTRELDETAILING@MAILHUB.COM</span>
    </li>
  </ul>
</section>

<section class="card card-back">
  <svg class="card-bg" viewBox="0 0 903 541" preserveAspectRatio="none" aria-hidden="true">
    <polygon points="0,0 290,0 260,541 0,541" fill="var(--red)"/>
  </svg>

  <p class="back-brand">KESTREL<br>DETAILING</p>
  <div class="back-art" role="img" aria-label="Illustration of a red sports car"></div>

  <div class="service-row" style="top:40px">
    <div class="price">$150</div>
    <div>
      <h2 class="service-title">INTERIOR DETAIL</h2>
      <p class="service-desc">Vacume &amp; deep clean of carpets &amp; upholstery or leather treatment, interior trim clean &amp; condition, window polish and treatment, steam clean and stain removal</p>
    </div>
  </div>
  <div class="divider" style="top:178px"></div>

  <div class="service-row" style="top:198px">
    <div class="price">$250</div>
    <div>
      <h2 class="service-title">EXTERIOR DETAIL</h2>
      <p class="service-desc">Extreme wash &amp; polish, exterior trim reviver &amp; protector window polish &amp; treatment, tyre dressing, engine bay cleaned</p>
    </div>
  </div>
  <div class="divider" style="top:314px"></div>

  <div class="service-row" style="top:334px">
    <div class="price">$350</div>
    <div>
      <h2 class="service-title">FULL EXTREME DETAIL</h2>
      <p class="service-desc">Extreme wash &amp; polish, tyre dressing, engine bay cleaned, vacume &amp; deep clean of carpets &amp; upholstery or leather treatment, interior &amp; exterior trim reviver &amp; protector, window polish and treatment,</p>
    </div>
  </div>
</section>

</body>
</html>
```